Business Card Design

I need a business card for my corporation. We are a fast food Mexican Taqueria located in San Jose, CA. I want the cards to include our business logo. The cards need to be simple but elegant. Our theme through out our locations is a beach feel atmosphere. I would like to see cards with a beach feeling. Our website is tacoslapalmera.net and it would be great if the cards matched our website.

Industry/Entity Type

Business

Contact Information for Business Card

Marisol Fuentes, VP
2417 Cedar Brook Ave
San Jose, CA 95482
Direct: 4087326159

```html
<!DOCTYPE html>
<html lang="en">
<head>
<meta charset="utf-8">
<title>La Palmera – Business Card</title>
<link rel="stylesheet" href="https://fonts.googleapis.com/css2?family=Cinzel:wght@400;500&family=Alegreya+Sans:wght@400&display=swap">
<style>
  :root {
    --backdrop: #e9e6e1;
    --card-white: #ffffff;
    --sun-yellow: #f6d312;
    --chili-red: #b31e27;
    --photo-top: #6fcfd6;
    --photo-bottom: #eef0ea;
  }
  * { margin: 0; padding: 0; box-sizing: border-box; }
  html, body { width: 1200px; height: 870px; overflow: hidden; }
  body { background: var(--backdrop); position: relative; }

  .card {
    position: absolute;
    top: 85px;
    width: 400px;
    height: 700px;
    background: var(--card-white);
    overflow: hidden;
    box-shadow: 0 6px 18px rgba(0,0,0,0.18);
  }
  .card--front { left: 170px; }
  .card--back { left: 630px; }

  .front-panels { position: absolute; inset: 0; width: 400px; height: 700px; }

  .front-details {
    position: absolute;
    left: 0; right: 0; top: 478px;
    text-align: center;
    color: var(--chili-red);
  }
  .brand-name {
    font-family: "Cinzel", serif;
    font-weight: 500;
    font-size: 30px;
    letter-spacing: 1px;
    color: var(--chili-red);
    white-space: nowrap;
  }
  .person-name {
    font-family: "Cinzel", serif;
    font-weight: 400;
    font-size: 27px;
    letter-spacing: 1.5px;
    margin-top: 22px;
    white-space: nowrap;
  }
  .contact {
    font-family: "Alegreya Sans", sans-serif;
    font-size: 19px;
    line-height: 1.35;
    margin-top: 16px;
  }
  .contact .phone { margin-bottom: 12px; }

  .photo-placeholder {
    position: absolute; inset: 0;
    background: linear-gradient(180deg, var(--photo-top) 0%, var(--photo-bottom) 100%);
  }
  .back-brand {
    position: absolute;
    left: 0; right: 0; top: 270px;
    text-align: center;
  }
  .back-brand .brand-name { font-size: 40px; }
</style>
</head>
<body>

  <section class="card card--front">
    <svg class="front-panels" viewBox="0 0 400 700" aria-hidden="true">
      <polygon points="0,0 192,0 208,292 0,468" fill="var(--sun-yellow)"/>
      <polygon points="200,0 400,0 400,410 216,294" fill="var(--chili-red)"/>
    </svg>
    <div class="front-details">
      <div class="brand-name">La Palmera</div>
      <div class="person-name">Marisol Fuentes</div>
      <div class="contact">
        <div class="phone">4087326159</div>
        <div>VP 2417 Cedar Brook Ave San Jose,</div>
        <div>CA 95482</div>
      </div>
    </div>
  </section>

  <section class="card card--back">
    <div class="photo-placeholder" role="img" aria-label="Full-bleed photograph of a tropical beach with turquoise water and white sand"></div>
    <div class="back-brand">
      <div class="brand-name">La Palmera</div>
    </div>
  </section>

</body>
</html>
```